Sparkling Wine Label

Need a new label design for my new product being launched. We are a wine company based in Los Angeles CA that currently produces two labels that were design on Pixel Harbor. Please review the attached file "Sparkling Label Design" which will have all details needed to complete. If not, please feel free to reach out by email.

Target Market(s)

Adults

Industry/Entity Type

It Company

Font styles to use
Script

Colors
8869ae
ffffff

Requirements
Must have
• Government Warning
• www.dorvanelwineco.com
• signature on back
• Script for the brand title: Velisse
Nice to have
• very elegant design.

```html
<!DOCTYPE html>
<html lang="en">
<head>
<meta charset="utf-8">
<title>Velisse Sparkling Riesling Label</title>
<link rel="stylesheet" href="https://fonts.googleapis.com/css2?family=Pinyon+Script&family=Great+Vibes&family=EB+Garamond:wght@500;600&family=Pathway+Gothic+One&family=Oswald:wght@400;500&family=Arimo&display=swap">
<style>
  :root {
    --page: #ffffff;
    --label: #94839c;
    --label-deep: #5f4b68;
    --label-line: #7a6884;
    --foliage: #8a7893;
    --ink: #2d2331;
    --muted: #4f3f57;
    --white: #ffffff;
    --soft-white: #f1ecf3;
    --gold: #c9a14c;
    --gold-dark: #7d5a22;
  }
  * { margin: 0; padding: 0; box-sizing: border-box; }
  html, body { width: 1200px; height: 900px; overflow: hidden; background: var(--page); }
  .canvas { position: relative; width: 1200px; height: 900px; }

  .label { position: absolute; background: var(--label); overflow: hidden; }
  .front-label { left: 82px; top: 239px; width: 614px; height: 369px; }
  .back-label { left: 749px; top: 239px; width: 369px; height: 369px; }

  .frame-band {
    position: absolute; left: 18px; top: 18px; right: 18px; bottom: 19px;
    border: 8px solid var(--label-deep);
  }
  .frame-line {
    position: absolute; left: 30px; top: 30px; right: 30px; bottom: 31px;
    border: 1px solid var(--label-line);
  }
  .foliage {
    position: absolute; top: 40px; width: 150px; height: 296px;
    background: radial-gradient(ellipse at center, var(--foliage) 0%, rgba(138,120,147,0) 72%);
  }
  .foliage-left { left: 36px; }
  .foliage-right { right: 36px; }

  .maker-mark {
    position: absolute; left: 372px; top: 44px; width: 100px; text-align: center;
    font-family: "EB Garamond", serif; font-weight: 600; font-size: 12px;
    letter-spacing: 2px; color: var(--gold);
  }
  .brand-script {
    position: absolute; font-family: "Pinyon Script", "Great Vibes", cursive; font-weight: 400;
    color: var(--white); white-space: nowrap; text-align: center;
    text-shadow: 0 2px 2px rgba(45,35,49,0.35);
  }
  .front-label .brand-script { left: 0; width: 614px; top: 82px; font-size: 128px; line-height: 1; }
  .varietal {
    position: absolute; left: 0; width: 100%; text-align: center;
    font-family: "EB Garamond", serif; font-weight: 500; color: var(--white);
  }
  .front-label .varietal { top: 236px; font-size: 23px; letter-spacing: 1px; }
  .region {
    position: absolute; left: 0; width: 100%; top: 271px; text-align: center;
    font-family: "EB Garamond", serif; font-weight: 600; font-size: 15px;
    letter-spacing: 2.5px; color: var(--ink);
  }
  .gold-rule {
    position: absolute; left: 240px; top: 307px; width: 142px; height: 2px;
    background: linear-gradient(90deg, rgba(201,161,76,0), var(--gold) 45%, var(--gold-dark) 55%, rgba(201,161,76,0));
  }
  .spec {
    position: absolute; top: 302px; font-family: "Pathway Gothic One", sans-serif;
    font-size: 16px; letter-spacing: 0.5px; color: var(--muted);
  }
  .spec-alcohol { left: 70px; }
  .spec-volume { right: 70px; }

  .back-label .brand-script { left: 0; width: 369px; top: 24px; font-size: 70px; line-height: 1; text-shadow: none; }
  .back-label .varietal { top: 118px; font-size: 17px; letter-spacing: 0.8px; }
  .government-warning {
    position: absolute; left: 26px; top: 164px; width: 318px;
    font-family: "Pathway Gothic One", sans-serif; font-size: 10.5px;
    line-height: 15.5px; letter-spacing: 0.55px; color: var(--ink); text-transform: uppercase;
  }
  .government-warning span { display: block; text-align: justify; text-align-last: justify; }
  .producer {
    position: absolute; left: 0; width: 100%; top: 248px; text-align: center;
    font-family: "Arimo", sans-serif; font-size: 12px; line-height: 21px; color: var(--soft-white);
  }
  .sulfites {
    position: absolute; left: 0; width: 100%; top: 293px; text-align: center;
    font-family: "Oswald", sans-serif; font-weight: 500; font-size: 14px;
    letter-spacing: 0.6px; color: var(--ink);
  }
  .website {
    position: absolute; left: 0; width: 100%; top: 323px; text-align: center;
    font-family: "Oswald", sans-serif; font-weight: 400; font-size: 13.5px;
    letter-spacing: 0.8px; color: var(--white);
  }
</style>
</head>
<body>
<main class="canvas">
  <section class="label front-label" aria-label="Front label">
    <div class="frame-band"></div>
    <div class="frame-line"></div>
    <div class="foliage foliage-left" role="img" aria-label="Faint leafy vine ornament"></div>
    <div class="foliage foliage-right" role="img" aria-label="Faint leafy vine ornament"></div>
    <div class="maker-mark">DORVANEL</div>
    <h1 class="brand-script">Velisse</h1>
    <p class="varietal">SPARKLING RIESLING</p>
    <p class="region">WASHINGTON</p>
    <div class="gold-rule"></div>
    <p class="spec spec-alcohol">ALC 12%</p>
    <p class="spec spec-volume">750 ML</p>
  </section>

  <section class="label back-label" aria-label="Back label">
    <h2 class="brand-script">Velisse</h2>
    <p class="varietal">SPARKLING RIESLING</p>
    <p class="government-warning">
      <span>Government Warning: (1) According to the Surgeon General, women should</span>
      <span>not drink alcoholic beverages during pregnancy because of the risk of</span>
      <span>birth defects. (2) Consumption of alcoholic beverages impairs your ability</span>
      <span>to drive a car or operate machinery, and may cause health problems.</span>
    </p>
    <p class="producer">Vinted and Bottled By Tidewater Cellars, Ceres Ca for<br>Dorvanel Wine Company, Los Angeles Ca</p>
    <p class="sulfites">CONTAINS SULFITES</p>
    <p class="website">www.dorvanelwineco.com</p>
  </section>
</main>
</body>
</html>
```